Brookfarrow Osteopathy and dry needling business card

Business card for Brookfarrow Osteopathy and Dry Needling.

Industry/Entity Type

Health

Contact Information for Business Card

I do not have a phone number yet. I also do not have an email address yet. The physical address is: 48 Lower Crane Street Brookfarrow The website is: www.brookfarrowosteosteopathy.example My details are: Dr Martin Pellowe, Osteopath (B.Clin.Sci (Ost) M.Ost BSC ECON (Hons)

Colors
0094D4
00A9DD
6FCCEA
C7EBF8
E9F6FB

Requirements
Must have
• logo on the back
Nice to have
• Maybe a space for me to write an appointment time and date on the card.

```html
<!DOCTYPE html>
<html lang="en">
<head>
<meta charset="utf-8">
<title>Brookfarrow Osteopathy and Dry Needling – Business Card</title>
<link rel="stylesheet" href="https://fonts.googleapis.com/css2?family=Poppins:wght@400;600&display=swap">
<style>
  :root {
    --page: #e9ecef;
    --card: #1b1b1d;
    --card-back: #121213;
    --blue: #0094d4;
    --blue-bright: #00a9dd;
    --text: #f2f2f2;
  }
  * { box-sizing: border-box; margin: 0; padding: 0; }
  html, body { width: 1200px; height: 874px; overflow: hidden; }
  body {
    background: var(--page);
    font-family: "Poppins", sans-serif;
    color: var(--text);
    position: relative;
  }
  .card {
    position: absolute;
    left: 250px;
    width: 700px;
    height: 400px;
    border-radius: 22px;
    overflow: hidden;
    box-shadow: 0 10px 30px rgba(0,0,0,0.18);
  }
  .card--back { top: 25px; background: var(--card-back); }
  .card--front { top: 449px; background: var(--card); }

  .back-pattern {
    position: absolute;
    inset: 0;
    background: linear-gradient(135deg, #101011 0%, #161617 50%, #3a3b3d 100%);
  }
  .back-brand {
    position: absolute;
    inset: 0;
    display: flex;
    align-items: center;
    justify-content: center;
    gap: 18px;
  }
  .back-brand__circle {
    width: 56px; height: 56px;
    border: 3px solid var(--blue-bright);
    border-radius: 50%;
    flex-shrink: 0;
  }
  .back-brand__name {
    font-size: 28px;
    font-weight: 600;
    line-height: 1.2;
    color: var(--blue-bright);
  }

  .identity { position: absolute; left: 42px; top: 52px; }
  .identity__name {
    font-weight: 600;
    font-size: 34px;
    line-height: 1.1;
    color: var(--blue);
  }
  .identity__credentials {
    margin-top: 6px;
    font-size: 17px;
    line-height: 1.35;
  }
  .address { margin-top: 18px; font-size: 17px; line-height: 1.35; }

  .contacts {
    position: absolute;
    left: 42px;
    top: 312px;
    list-style: none;
    font-size: 16px;
    line-height: 1.6;
  }
  .contacts li { display: flex; align-items: center; gap: 10px; }
  .contacts svg { width: 15px; height: 15px; flex-shrink: 0; }

  .appointment {
    position: absolute;
    left: 450px;
    top: 180px;
    font-size: 16px;
    line-height: 1;
  }
  .appointment__row { display: flex; align-items: flex-end; gap: 6px; margin-bottom: 26px; }
  .appointment__line {
    display: inline-flex;
    align-items: flex-end;
    width: 180px;
    height: 18px;
    padding-left: 60px;
    border-bottom: 1.5px solid var(--text);
    font-size: 15px;
  }

  .brand {
    position: absolute;
    right: 36px;
    bottom: 32px;
    display: flex;
    align-items: center;
    gap: 12px;
  }
  .brand__circle {
    width: 40px; height: 40px;
    border: 2px solid var(--blue-bright);
    border-radius: 50%;
    flex-shrink: 0;
  }
  .brand__name {
    font-size: 15px;
    font-weight: 600;
    line-height: 1.3;
    color: var(--blue-bright);
  }
</style>
</head>
<body>

  <section class="card card--back">
    <div class="back-pattern" role="img" aria-label="Tonal repeat pattern of the Brookfarrow practice emblem on black"></div>
    <div class="back-brand">
      <span class="back-brand__circle"></span>
      <span class="back-brand__name">Brookfarrow Osteopathy<br>and Dry Needling</span>
    </div>
  </section>

  <section class="card card--front">
    <div class="identity">
      <h1 class="identity__name">Dr Martin Pellowe,</h1>
      <p class="identity__credentials">Osteopath (B.Clin.Sci (Ost)<br>M.Ost BSC ECON (Hons)</p>
      <p class="address">48 Lower Crane Street<br>Brookfarrow</p>
    </div>

    <ul class="contacts">
      <li>
        <svg viewBox="0 0 24 24" aria-hidden="true"><circle cx="12" cy="12" r="9" fill="none" stroke="#0094d4" stroke-width="2"/><path d="M3 12h18M12 3c3 3 3 15 0 18M12 3c-3 3-3 15 0 18" fill="none" stroke="#0094d4" stroke-width="1.6"/></svg>
        www.brookfarrowosteosteopathy.example
      </li>
    </ul>

    <div class="appointment">
      <div class="appointment__row"><span>DATE</span><span class="appointment__line">/</span></div>
      <div class="appointment__row"><span>TIME</span><span class="appointment__line">:</span></div>
    </div>

    <div class="brand">
      <span class="brand__circle"></span>
      <span class="brand__name">Brookfarrow Osteopathy<br>and Dry Needling</span>
    </div>
  </section>

</body>
</html>
```